Design of Product Brochure

TLM Survey Advisory, based in Namibia, is launching a premium charcoal brand: Embera Charcoal. We manufacture two distinct, high-quality product lines: one for the serious home barbecuer and one for professional restaurant kitchens.
The objective of this project is to create a cohesive and compelling visual identity across a product brochure (for B2B sales and high-end B2C) and a marketing website. The designs must elevate Embera Charcoal from a simple commodity to a premium, trusted fuel choice, emphasizing its Namibian origin, scientific backing, and superior performance.

```html
<!DOCTYPE html>
<html lang="en">
<head>
<meta charset="utf-8">
<title>Embera Charcoal Brochure Spread</title>
<link href="https://fonts.googleapis.com/css2?family=Montserrat:wght@700;800&family=Roboto:wght@400;500;700&display=swap" rel="stylesheet">
<style>
:root{
  --red:#d32f2a;
  --ink:#1e1e1e;
  --black:#0d0d0d;
  --cream-a:#efe4dc;
  --cream-b:#f8efe6;
  --paper:#f7f6f4;
  --table-head:#e3d6d2;
  --table-cell:#f1ebe8;
  --table-line:#b9aaa6;
  --icon-bg:#e2e0de;
  --stage:#e9e9e9;
}
*{box-sizing:border-box;margin:0;padding:0}
html,body{width:1200px;height:960px;overflow:hidden;background:var(--stage)}
body{font-family:"Roboto",Arial,sans-serif;color:var(--ink);position:relative}
.spread{position:absolute;left:25px;top:67px;width:1150px;height:825px;background:linear-gradient(90deg,var(--cream-a),var(--cream-b));box-shadow:0 6px 18px rgba(0,0,0,.12)}
.spread::after{content:"";position:absolute;left:580px;top:0;width:1px;height:100%;background:rgba(0,0,0,.06)}
.hero{position:absolute;left:0;top:0;width:740px;height:338px;background:linear-gradient(160deg,#c9c2a8 0%,#8fa06a 35%,#5d7a3e 65%,#3f5a2c 100%)}
.features{position:absolute;left:740px;top:0;width:410px;height:338px;background:var(--paper);padding:88px 30px 0 38px}
.features h2{font-family:"Montserrat",Arial,sans-serif;font-weight:800;font-size:19px;color:var(--red);margin-bottom:10px}
.feature{display:flex;gap:12px;margin-bottom:12px}
.feature-icon{flex:none;width:42px;height:42px;border-radius:50%;background:var(--icon-bg);display:flex;align-items:center;justify-content:center;margin-top:4px}
.feature h3{font-size:12px;font-weight:500;color:var(--red);line-height:1.1}
.feature p{font-size:12px;line-height:1.15;color:var(--ink)}
.grade{position:absolute;top:362px;width:575px;height:450px}
.grade.restaurant{left:0}
.grade.barbecue{left:581px}
.grade-banner{position:absolute;left:0;top:0;width:388px;height:38px;background:var(--red);color:#fff;font-family:"Montserrat",Arial,sans-serif;font-weight:800;font-size:21px;line-height:40px;padding-left:38px}
.grade-rule{position:absolute;left:388px;top:37px;width:154px;height:1.5px;background:var(--red)}
.label{position:absolute;left:38px;width:200px;height:20px;background:var(--black);color:#fff;font-size:13px;font-weight:500;line-height:20px;padding-left:21px}
.benefits{position:absolute;left:58px;top:76px;list-style:none;font-size:10.6px;line-height:12.1px}
.benefits li{position:relative;padding-left:16px}
.benefits li::before{content:"";position:absolute;left:0;top:3.5px;width:6px;height:6px;border-radius:50%;background:var(--red)}
.benefits b{font-weight:700}
table{position:absolute;border-collapse:collapse;font-size:9px;text-align:center}
th,td{border:1px solid var(--table-line);padding:1px 3px;line-height:1.1}
th{background:var(--table-head);font-weight:400}
td{background:var(--table-cell)}
.tech{left:38px;top:190px;width:504px}
.tech td{height:34px}
.chem{left:38px;top:280px;width:328px}
.chem td{height:16px}
.chem th{height:24px}
.bag{position:absolute;left:415px;top:262px;width:72px;height:158px;border-radius:6px 6px 4px 4px;background:linear-gradient(180deg,#222 0%,#111 70%,var(--red) 100%)}
</style>
</head>
<body>
<main class="spread">
  <div class="hero" role="img" aria-label="Photo of a family enjoying a garden barbecue with apples and a kettle grill"></div>

  <section class="features">
    <h2>EMBERA KEY FEATURES</h2>
    <div class="feature">
      <div class="feature-icon"><svg width="22" height="22" viewBox="0 0 22 22"><rect x="9" y="2" width="4" height="12" rx="2" fill="none" stroke="#d32f2a" stroke-width="1.6"/><circle cx="11" cy="17" r="3.5" fill="#d32f2a"/><path d="M15 5h3M15 8h3M15 11h3" stroke="#d32f2a" stroke-width="1.2"/></svg></div>
      <div><h3>HIGH HEAT</h3><p>Embera Charcoal products are designed to achieve and maintain high temperatures, perfect for grilling, smoking, and roasting.</p></div>
    </div>
    <div class="feature">
      <div class="feature-icon"><svg width="22" height="22" viewBox="0 0 22 22"><path d="M11 2c2 4 6 6 6 11a6 6 0 0 1-12 0c0-3 2-5 3-6 0 2 1 3 2 3 0-3 0-5 1-8z" fill="#f08a24"/><circle cx="11" cy="14" r="3.2" fill="#fff"/><path d="M11 12.3v1.9l1.2.8" stroke="#d32f2a" stroke-width="1" fill="none"/></svg></div>
      <div><h3>BURN TIME</h3><p>Engineered to burn longer than standard charcoal, reducing the need for frequent refuelling and ensuring a more convenient cooking experience.</p></div>
    </div>
    <div class="feature">
      <div class="feature-icon"><svg width="22" height="22" viewBox="0 0 22 22"><path d="M11 2c2 3 5 5 5 9a5 5 0 0 1-10 0c0-2 1-4 2-5 0 2 1 2 2 2 0-2 0-4 1-6z" fill="#d32f2a"/><path d="M4 16l14 4M18 16L4 20" stroke="#7a4a2a" stroke-width="2.2" stroke-linecap="round"/></svg></div>
      <div><h3>PRODUCE LESS ASH</h3><p>Produces minimal ash, making cleanup easier and enhancing the overall grilling experience.</p></div>
    </div>
  </section>

  <section class="grade restaurant">
    <div class="grade-banner">EMBERA RESTAURANT GRADE</div>
    <div class="grade-rule"></div>
    <div class="label" style="top:48px">KEY PRODUCT BENEFITS</div>
    <ul class="benefits">
      <li><b>Natural Flavor</b> – Adds a distinct smoky, wood-fired taste to food.</li>
      <li><b>High Heat Output</b> – Burns hotter than briquettes, ideal for searing.</li>
      <li><b>Quick to Light</b> – Heats up faster compared to compressed charcoal.</li>
      <li><b>Low Ash Residue</b> – Leaves less waste, making cleanup easier.</li>
      <li><b>Versatile Cooking</b> – Suitable for grilling, smoking, and slow cooking.</li>
      <li><b>100% Natural Hardwood</b> – No added chemicals, binders, or fillers.</li>
    </ul>
    <div class="label" style="top:156px">TECHNICAL DATA</div>
    <table class="tech">
      <tr><th>EAN</th><th>Net weight</th><th>Bag size</th><th>Charcoal pieces</th><th>Bulk density</th><th>Calorific value, Q</th><th>Warranty</th></tr>
      <tr><td>26461222549</td><td>5 Kg</td><td>260x680x140mm</td><td>&gt;80mm 30%<br>20-80mm 50%<br>&lt;20mm 20%</td><td>155 kg/m3</td><td>8083 kg/m3<br>33.84 MJ/kg<br>9.40 MWh/t</td><td>EU</td></tr>
    </table>
    <div class="label" style="top:245px">CHEMICAL TEST RESULTS</div>
    <table class="chem">
      <tr><th>Nr.</th><th>Characteristics<br>of verifications</th><th>Unity of<br>measure</th><th>Methods</th><th>Results</th><th>EN 1860-2: 2005 (E)<br>requirements</th></tr>
      <tr><td>1.</td><td>Moisture</td><td>%</td><td>ISO 579</td><td>4.08</td><td>Max 8.0 %</td></tr>
      <tr><td>2.</td><td>Ash content</td><td>%</td><td>ISO 1171</td><td>2.30</td><td>Max 8.0 %</td></tr>
      <tr><td rowspan="3">3.</td><td rowspan="3">Calorific value,<br>Q</td><td>kcal/kg</td><td rowspan="3">ISO 1928</td><td>8083</td><td rowspan="3">-</td></tr>
      <tr><td>MJ/kg</td><td>33.84</td></tr>
      <tr><td>MWh/t</td><td>9.40</td></tr>
      <tr><td>4.</td><td>Volatiles</td><td>%</td><td>ISO 562</td><td>13.35</td><td>-</td></tr>
      <tr><td>5.</td><td>Fixed carbon</td><td>%</td><td>DIN 51749</td><td>84.35</td><td>Min 75.00 %</td></tr>
      <tr><td>6.</td><td>Bulk density</td><td>kg/m3</td><td>EN 15103</td><td>155</td><td>Min 130</td></tr>
    </table>
    <div class="bag" role="img" aria-label="Product shot of a 5 kg Embera Charcoal bag"></div>
  </section>

  <section class="grade barbecue">
    <div class="grade-banner">EMBERA BARBECUE GRADE</div>
    <div class="grade-rule"></div>
    <div class="label" style="top:48px">KEY PRODUCT BENEFITS</div>
    <ul class="benefits">
      <li><b>Natural Flavor</b> – Adds a distinct smoky, wood-fired taste to food.</li>
      <li><b>High Heat Output</b> – Burns hotter than briquettes, ideal for searing.</li>
      <li><b>Quick to Light</b> – Heats up faster compared to compressed charcoal.</li>
      <li><b>Low Ash Residue</b> – Leaves less waste, making cleanup easier.</li>
      <li><b>Versatile Cooking</b> – Suitable for grilling, smoking, and slow cooking.</li>
      <li><b>100% Natural Hardwood</b> – No added chemicals, binders, or fillers.</li>
    </ul>
    <div class="label" style="top:156px">TECHNICAL DATA</div>
    <table class="tech" style="width:494px">
      <tr><th>EAN</th><th>Net weight</th><th>Bag size</th><th>Charcoal pieces</th><th>Bulk density</th><th>Calorific value, Q</th><th>Warranty</th></tr>
      <tr><td>26461222549</td><td>5 Kg</td><td>260x680x140mm</td><td>&gt;80mm 30%<br>20-80mm 50%<br>&lt;20mm 20%</td><td>155 kg/m3</td><td>8083 kg/m3<br>33.84 MJ/kg<br>9.40 MWh/t</td><td>EU</td></tr>
    </table>
    <div class="label" style="top:245px">CHEMICAL TEST RESULTS</div>
    <table class="chem" style="width:320px">
      <tr><th>Nr.</th><th>Characteristics<br>of verifications</th><th>Unity of<br>measure</th><th>Methods</th><th>Results</th><th>EN 1860-2: 2005 (E)<br>requirements</th></tr>
      <tr><td>1.</td><td>Moisture</td><td>%</td><td>ISO 579</td><td>4.08</td><td>Max 8.0 %</td></tr>
      <tr><td>2.</td><td>Ash content</td><td>%</td><td>ISO 1171</td><td>2.30</td><td>Max 8.0 %</td></tr>
      <tr><td rowspan="3">3.</td><td rowspan="3">Calorific value,<br>Q</td><td>kcal/kg</td><td rowspan="3">ISO 1928</td><td>8083</td><td rowspan="3">-</td></tr>
      <tr><td>MJ/kg</td><td>33.84</td></tr>
      <tr><td>MWh/t</td><td>9.40</td></tr>
      <tr><td>4.</td><td>Volatiles</td><td>%</td><td>ISO 562</td><td>13.35</td><td>-</td></tr>
      <tr><td>5.</td><td>Fixed carbon</td><td>%</td><td>DIN 51749</td><td>84.35</td><td>Min 75.00 %</td></tr>
      <tr><td>6.</td><td>Bulk density</td><td>kg/m3</td><td>EN 15103</td><td>155</td><td>Min 130</td></tr>
    </table>
    <div class="bag" style="left:404px" role="img" aria-label="Product shot of a 5 kg Embera Charcoal bag"></div>
  </section>
</main>
</body>
</html>
```